Lanternwick Pathway Ledger Basics

size of the ad - 8”x 10.75" plus 0.25" bleed
I would like an ad for a magazine that will stand out and make people want to read the ad.
The ad should not be crowded and people reading the ad will be able to read the text.
I would like it to be a creative and modern-day design.
the list of topics should not be the focus of the ad.
the text is attached.
If you decide to use people in the ad then please no ladies.
please note that leave over 1 inch for the bottom of the footer

```html
<!DOCTYPE html>
<html lang="en">
<head>
<meta charset="utf-8">
<title>Lanternwick Pathway Ledger Basics – Course Ad</title>
<link rel="stylesheet" href="https://fonts.googleapis.com/css2?family=Montserrat:wght@400;500;600;700;800;900&family=Questrial&display=swap">
<style>
  :root {
    --navy: #20205e;
    --navy-deep: #0f2656;
    --red: #b71f28;
    --white: #ffffff;
    --ink: #2b2b33;
    --page: #e9e9ec;
    --sans: "Montserrat", Arial, sans-serif;
    --soft: "Questrial", "Helvetica Neue", sans-serif;
  }
  * { margin: 0; padding: 0; box-sizing: border-box; }
  html, body { width: 1200px; height: 1085px; overflow: hidden; background: var(--page); }
  .ad {
    position: absolute; left: 211px; top: 20px;
    width: 778px; height: 1045px;
    background: var(--white); overflow: hidden;
    box-shadow: 0 4px 18px rgba(0,0,0,.18);
    font-family: var(--sans); color: var(--white);
  }
  .ad-art { position: absolute; inset: 0; }
  .title {
    position: absolute; left: 36px; top: 38px;
    font-weight: 900; font-size: 92px; letter-spacing: -1px; line-height: 1;
    color: var(--navy);
  }
  .course-pill {
    position: absolute; left: 20px; top: 141px; width: 353px; height: 69px;
    background: var(--red); border-radius: 35px;
    font-weight: 700; font-size: 66px; line-height: 69px; padding-left: 27px;
    letter-spacing: 1px;
  }
  .course-name {
    position: absolute; left: 47px; top: 312px;
    font-weight: 500; font-size: 31px; line-height: 42px; text-transform: uppercase;
  }
  .rule { position: absolute; left: 49px; top: 409px; width: 139px; height: 3px; background: var(--red); }
  .tagline {
    position: absolute; left: 51px; top: 424px;
    font-family: var(--soft); font-size: 25px; line-height: 31px; letter-spacing: .5px;
  }
  .location-pill {
    position: absolute; left: 0; top: 533px; width: 243px; height: 47px;
    background: var(--red); border-radius: 0 24px 24px 0;
    font-weight: 400; font-size: 27px; line-height: 47px; padding-left: 53px;
  }
  .schedule {
    position: absolute; left: 55px; top: 598px;
    font-weight: 700; font-size: 28px; line-height: 36px; text-transform: uppercase;
  }
  .details {
    position: absolute; left: 56px; top: 674px;
    font-family: var(--soft); font-size: 22px; line-height: 30px;
  }
  .topics-tab {
    position: absolute; left: 0; top: 783px; width: 252px; height: 44px;
    background: var(--navy-deep); border-radius: 0 30px 0 0;
    font-weight: 700; font-size: 16px; line-height: 44px; padding-left: 47px;
  }
  .topics {
    position: absolute; top: 843px; list-style: none;
    color: var(--ink); font-size: 15px; line-height: 26.5px;
  }
  .topics--left { left: 47px; }
  .topics--right { left: 364px; }
  .topics li { display: flex; align-items: center; gap: 8px; }
  .topics svg { width: 14px; height: 14px; flex: none; }
  .early-bird {
    position: absolute; left: 592px; top: 770px; width: 170px; height: 170px;
    border-radius: 50%; background: radial-gradient(circle at 40% 35%, #1d3d7a, var(--navy-deep));
    box-shadow: 0 3px 8px rgba(0,0,0,.25);
    display: flex; flex-direction: column; align-items: center; justify-content: center;
    text-align: center;
  }
  .early-bird::before {
    content: ""; position: absolute; inset: 7px; border: 2px solid var(--red); border-radius: 50%;
  }
  .early-bird h2 { font-weight: 700; font-size: 16px; line-height: 19px; }
  .early-bird hr { width: 104px; border: 0; border-top: 1px solid var(--red); margin: 4px 0 5px; }
  .early-bird p { font-size: 12px; line-height: 14.5px; width: 110px; }
  .phone {
    position: absolute; left: 42px; top: 993px; height: 36px;
    display: flex; align-items: center; gap: 13px;
    font-weight: 700; font-size: 28px; letter-spacing: 2.5px;
  }
  .web {
    position: absolute; left: 400px; top: 993px; height: 30px;
    display: flex; align-items: center; gap: 12px;
    font-family: var(--soft); font-size: 26px; letter-spacing: .5px;
  }
</style>
</head>
<body>
<main class="ad">
  <svg class="ad-art" viewBox="0 0 778 1045" width="778" height="1045" aria-hidden="false">
    <defs>
      <linearGradient id="sceneTone" x1="0" y1="0" x2="0" y2="1">
        <stop offset="0" stop-color="#4a5066"/>
        <stop offset=".45" stop-color="#5a5a63"/>
        <stop offset=".75" stop-color="#3f4a3a"/>
        <stop offset="1" stop-color="#2f3a2c"/>
      </linearGradient>
      <linearGradient id="listTone" x1="0" y1="0" x2="1" y2="1">
        <stop offset="0" stop-color="#ffffff"/>
        <stop offset=".5" stop-color="#eef0f3"/>
        <stop offset="1" stop-color="#ffffff"/>
      </linearGradient>
    </defs>
    <path d="M770 0 Q760 190 620 255 L778 255 L778 0 Z" fill="#7d8399"/>
    <path role="img" aria-label="Photo: suburban house at dusk with lawn, and a smiling man in shirt and tie with arms crossed"
          d="M0 260 L620 260 Q745 215 778 30 L778 819 L0 819 Z" fill="url(#sceneTone)"/>
    <rect x="0" y="819" width="778" height="175" fill="url(#listTone)"/>
    <path d="M0 993 L340 993 Q365 993 378 1000 L778 1000 L778 1045 L0 1045 Z" fill="var(--red)"/>
    <path d="M378 1000 L778 1000 L778 1037 L386 1037 Q380 1016 378 1000 Z" fill="var(--navy-deep)"/>
  </svg>

  <h1 class="title">REAL ESTATE</h1>
  <div class="course-pill">COURSE</div>

  <h2 class="course-name">Lanternwick Pathway<br>Ledger Basics</h2>
  <div class="rule"></div>
  <p class="tagline">Investing in knowledge<br>is investing in opportunities.</p>

  <div class="location-pill">ELMBROOK</div>
  <p class="schedule">10 -Tuesday<br>Evenings Sessions</p>
  <p class="details">Starting Feb.28<br>Limited Partial Scholarships</p>

  <div class="topics-tab">Topics: partial listing</div>
  <ul class="topics topics--left">
    <li><svg viewBox="0 0 14 14"><circle cx="7" cy="7" r="6" fill="none" stroke="#b71f28" stroke-width="1.3"/><path d="M6 4.5 L8.5 7 L6 9.5" fill="none" stroke="#b71f28" stroke-width="1.4"/></svg>Real estate investment strategies</li>
    <li><svg viewBox="0 0 14 14"><circle cx="7" cy="7" r="6" fill="none" stroke="#b71f28" stroke-width="1.3"/><path d="M6 4.5 L8.5 7 L6 9.5" fill="none" stroke="#b71f28" stroke-width="1.4"/></svg>Due diligence</li>
    <li><svg viewBox="0 0 14 14"><circle cx="7" cy="7" r="6" fill="none" stroke="#b71f28" stroke-width="1.3"/><path d="M6 4.5 L8.5 7 L6 9.5" fill="none" stroke="#b71f28" stroke-width="1.4"/></svg>Financing</li>
    <li><svg viewBox="0 0 14 14"><circle cx="7" cy="7" r="6" fill="none" stroke="#b71f28" stroke-width="1.3"/><path d="M6 4.5 L8.5 7 L6 9.5" fill="none" stroke="#b71f28" stroke-width="1.4"/></svg>Underwriting</li>
    <li><svg viewBox="0 0 14 14"><circle cx="7" cy="7" r="6" fill="none" stroke="#b71f28" stroke-width="1.3"/><path d="M6 4.5 L8.5 7 L6 9.5" fill="none" stroke="#b71f28" stroke-width="1.4"/></svg>Property management</li>
  </ul>
  <ul class="topics topics--right">
    <li><svg viewBox="0 0 14 14"><circle cx="7" cy="7" r="6" fill="none" stroke="#b71f28" stroke-width="1.3"/><path d="M6 4.5 L8.5 7 L6 9.5" fill="none" stroke="#b71f28" stroke-width="1.4"/></svg>Real estate Legal basics</li>
    <li><svg viewBox="0 0 14 14"><circle cx="7" cy="7" r="6" fill="none" stroke="#b71f28" stroke-width="1.3"/><path d="M6 4.5 L8.5 7 L6 9.5" fill="none" stroke="#b71f28" stroke-width="1.4"/></svg>Sourcing deals</li>
    <li><svg viewBox="0 0 14 14"><circle cx="7" cy="7" r="6" fill="none" stroke="#b71f28" stroke-width="1.3"/><path d="M6 4.5 L8.5 7 L6 9.5" fill="none" stroke="#b71f28" stroke-width="1.4"/></svg>Syndication</li>
    <li><svg viewBox="0 0 14 14"><circle cx="7" cy="7" r="6" fill="none" stroke="#b71f28" stroke-width="1.3"/><path d="M6 4.5 L8.5 7 L6 9.5" fill="none" stroke="#b71f28" stroke-width="1.4"/></svg>Dealing with brokers</li>
    <li><svg viewBox="0 0 14 14"><circle cx="7" cy="7" r="6" fill="none" stroke="#b71f28" stroke-width="1.3"/><path d="M6 4.5 L8.5 7 L6 9.5" fill="none" stroke="#b71f28" stroke-width="1.4"/></svg>Tax fundamentals</li>
  </ul>

  <aside class="early-bird">
    <h2>EARLY<br>BIRD SPECIAL</h2>
    <hr>
    <p>For those that started or would like to go into real estate</p>
  </aside>

  <div class="phone">
    <svg width="36" height="36" viewBox="0 0 36 36" aria-hidden="true">
      <circle cx="18" cy="18" r="16.5" fill="#20205e" stroke="#fff" stroke-width="2.5"/>
      <path d="M13 10 Q11 11 11.5 15 Q13 22 20 25.5 Q24 27 25.5 24.5 L23 21.5 Q21.5 21 20.5 22.5 Q16.5 20 15 16 Q16.5 15 16 13.5 Z" fill="#fff"/>
    </svg>
    <span>0198 765 432</span>
  </div>
  <div class="web">
    <svg width="20" height="20" viewBox="0 0 20 20" aria-hidden="true">
      <circle cx="10" cy="10" r="9" fill="#b71f28"/>
      <g fill="none" stroke="#fff" stroke-width="1"><circle cx="10" cy="10" r="6.5"/><ellipse cx="10" cy="10" rx="3" ry="6.5"/><path d="M3.5 10 H16.5 M5 6.5 H15 M5 13.5 H15"/></g>
    </svg>
    <span>harrowgatelearning.com</span>
  </div>
</main>
</body>
</html>
```